Cigar Ring Design

we are working on a project, which is an eCommerce store for cigars, now instead of selling all kind of existing brands this project is based on a TabacoMillDepot concept where an outlet is linked to an actual Cigar factory,
so the cigar lines sold will come out under a TMD (TabacoMillDepot) brand consisting of various labels, (think Barney Cotter, Ochre Crest, Slate Crest etc) I had an idea for the Cigar Rings for this project, where I put TM in an O (circle) of which I made mock ups (see attachement), now I am not a designer, I am sure a real designer can come up with something more stylish and unique.

```html
<!DOCTYPE html>
<html lang="en">
<head>
<meta charset="utf-8">
<title>TabacoMillDepot – Cigar Ring Series</title>
<link rel="stylesheet" href="https://fonts.googleapis.com/css2?family=Cinzel:wght@400;500&display=swap">
<style>
  :root {
    --frame: #000000;
    --board: #616161;
    --foil-stage: #141414;
    --accent: #f6c842;
    --accent-dark: #c9a43a;
    --band-onyx: #050505;
    --band-fern: #33754a;
    --band-pewter: #d6d6d6;
    --band-amber: #a77d05;
    --band-ochre: #dc2b2e;
    --band-slate: #1f2394;
    --foil: #e9dca0;
  }
  html, body {
    margin: 0;
    padding: 0;
    overflow: hidden;
    background: var(--frame);
  }
  .sheet {
    position: relative;
    width: 970px;
    height: 1200px;
    background: var(--frame);
    overflow: hidden;
    font-family: "Cinzel", Georgia, serif;
  }
  .band-board {
    position: absolute;
    left: 32px;
    top: 27px;
    width: 911px;
    height: 645px;
    background: var(--board);
  }
  .band {
    position: absolute;
    width: 342px;
    height: 130px;
    overflow: visible;
    filter: drop-shadow(3px 4px 3px rgba(0,0,0,0.45));
  }
  .band .rule { stroke: var(--ink); stroke-width: 2; }
  .band .tab-ring { fill: none; stroke: var(--ink); stroke-width: 2.2; }
  .band .house-name {
    fill: var(--ink);
    font-size: 10px;
    font-weight: 500;
    letter-spacing: 0.3px;
  }
  .band .label-name {
    fill: var(--ink);
    font-size: 19px;
    font-weight: 400;
    letter-spacing: 0.5px;
  }
  .col-left { left: 88px; }
  .col-right { left: 483px; }
  .row-1 { top: 88px; }
  .row-2 { top: 260px; }
  .row-3 { top: 432px; }

  .band-onyx   { --fill: var(--band-onyx);   --ink: var(--accent); }
  .band-fern   { --fill: var(--band-fern);   --ink: var(--accent); }
  .band-pewter { --fill: var(--band-pewter); --ink: var(--accent-dark); }
  .band-amber  { --fill: var(--band-amber);  --ink: #f7d35a; }
  .band-ochre  { --fill: var(--band-ochre);  --ink: var(--accent); }
  .band-slate  { --fill: var(--band-slate);  --ink: var(--accent); }
  .band .body { fill: var(--fill); }

  .foil-board {
    position: absolute;
    left: 32px;
    top: 693px;
    width: 911px;
    height: 479px;
    background: var(--foil-stage);
  }
  .foil-board svg { position: absolute; left: 0; top: 0; }
  .foil-board .rule { stroke: var(--foil); stroke-width: 3; }
  .foil-board .house-name {
    fill: var(--foil);
    font-size: 30px;
    font-weight: 500;
  }
  .foil-board .label-name {
    fill: var(--foil);
    font-size: 56px;
    font-weight: 400;
    letter-spacing: 1px;
  }
</style>
</head>
<body>
<main class="sheet">
  <section class="band-board" aria-label="Cigar ring colour series">
    <svg class="band band-onyx col-left row-1" viewBox="0 0 342 130" role="img" aria-label="Onyx Crest ring">
      <path class="body" d="M8,28.5 H32 C48,28.5 58,2 100,2 C142,2 152,28.5 168,28.5 H316 a8,8 0 0 1 8,8 V93.5 a8,8 0 0 1 -8,8 H168 C152,101.5 142,128 100,128 C58,128 48,101.5 32,101.5 H8 a8,8 0 0 1 -8,-8 V36.5 a8,8 0 0 1 8,-8 Z"/>
      <circle class="body" cx="324" cy="65" r="17"/>
      <line class="rule" x1="11" y1="44" x2="42" y2="44"/><line class="rule" x1="11" y1="85" x2="42" y2="85"/>
      <line class="rule" x1="150" y1="44" x2="306" y2="44"/><line class="rule" x1="150" y1="85" x2="306" y2="85"/>
      <text class="house-name" x="100" y="69" text-anchor="middle">TabacoMillDepot</text>
      <text class="label-name" x="228" y="72" text-anchor="middle">Onyx Crest</text>
      <circle class="tab-ring" cx="324" cy="65" r="12"/>
    </svg>

    <svg class="band band-fern col-right row-1" viewBox="0 0 342 130" role="img" aria-label="Fern Crest ring">
      <path class="body" d="M8,28.5 H32 C48,28.5 58,2 100,2 C142,2 152,28.5 168,28.5 H316 a8,8 0 0 1 8,8 V93.5 a8,8 0 0 1 -8,8 H168 C152,101.5 142,128 100,128 C58,128 48,101.5 32,101.5 H8 a8,8 0 0 1 -8,-8 V36.5 a8,8 0 0 1 8,-8 Z"/>
      <circle class="body" cx="324" cy="65" r="17"/>
      <line class="rule" x1="11" y1="44" x2="42" y2="44"/><line class="rule" x1="11" y1="85" x2="42" y2="85"/>
      <line class="rule" x1="150" y1="44" x2="306" y2="44"/><line class="rule" x1="150" y1="85" x2="306" y2="85"/>
      <text class="house-name" x="100" y="69" text-anchor="middle">TabacoMillDepot</text>
      <text class="label-name" x="228" y="72" text-anchor="middle">Fern Crest</text>
      <circle class="tab-ring" cx="324" cy="65" r="12"/>
    </svg>

    <svg class="band band-pewter col-left row-2" viewBox="0 0 342 130" role="img" aria-label="Pewter Crest ring">
      <path class="body" d="M8,28.5 H32 C48,28.5 58,2 100,2 C142,2 152,28.5 168,28.5 H316 a8,8 0 0 1 8,8 V93.5 a8,8 0 0 1 -8,8 H168 C152,101.5 142,128 100,128 C58,128 48,101.5 32,101.5 H8 a8,8 0 0 1 -8,-8 V36.5 a8,8 0 0 1 8,-8 Z"/>
      <circle class="body" cx="324" cy="65" r="17"/>
      <line class="rule" x1="11" y1="44" x2="42" y2="44"/><line class="rule" x1="11" y1="85" x2="42" y2="85"/>
      <line class="rule" x1="150" y1="44" x2="306" y2="44"/><line class="rule" x1="150" y1="85" x2="306" y2="85"/>
      <text class="house-name" x="100" y="69" text-anchor="middle">TabacoMillDepot</text>
      <text class="label-name" x="228" y="72" text-anchor="middle">Pewter Crest</text>
      <circle class="tab-ring" cx="324" cy="65" r="12"/>
    </svg>

    <svg class="band band-amber col-right row-2" viewBox="0 0 342 130" role="img" aria-label="Amber Crest ring">
      <path class="body" d="M8,28.5 H32 C48,28.5 58,2 100,2 C142,2 152,28.5 168,28.5 H316 a8,8 0 0 1 8,8 V93.5 a8,8 0 0 1 -8,8 H168 C152,101.5 142,128 100,128 C58,128 48,101.5 32,101.5 H8 a8,8 0 0 1 -8,-8 V36.5 a8,8 0 0 1 8,-8 Z"/>
      <circle class="body" cx="324" cy="65" r="17"/>
      <line class="rule" x1="11" y1="44" x2="42" y2="44"/><line class="rule" x1="11" y1="85" x2="42" y2="85"/>
      <line class="rule" x1="150" y1="44" x2="306" y2="44"/><line class="rule" x1="150" y1="85" x2="306" y2="85"/>
      <text class="house-name" x="100" y="69" text-anchor="middle">TabacoMillDepot</text>
      <text class="label-name" x="228" y="72" text-anchor="middle">Amber Crest</text>
      <circle class="tab-ring" cx="324" cy="65" r="12"/>
    </svg>

    <svg class="band band-ochre col-left row-3" viewBox="0 0 342 130" role="img" aria-label="Ochre Crest ring">
      <path class="body" d="M8,28.5 H32 C48,28.5 58,2 100,2 C142,2 152,28.5 168,28.5 H316 a8,8 0 0 1 8,8 V93.5 a8,8 0 0 1 -8,8 H168 C152,101.5 142,128 100,128 C58,128 48,101.5 32,101.5 H8 a8,8 0 0 1 -8,-8 V36.5 a8,8 0 0 1 8,-8 Z"/>
      <circle class="body" cx="324" cy="65" r="17"/>
      <line class="rule" x1="11" y1="44" x2="42" y2="44"/><line class="rule" x1="11" y1="85" x2="42" y2="85"/>
      <line class="rule" x1="150" y1="44" x2="306" y2="44"/><line class="rule" x1="150" y1="85" x2="306" y2="85"/>
      <text class="house-name" x="100" y="69" text-anchor="middle">TabacoMillDepot</text>
      <text class="label-name" x="228" y="72" text-anchor="middle">Ochre Crest</text>
      <circle class="tab-ring" cx="324" cy="65" r="12"/>
    </svg>

    <svg class="band band-slate col-right row-3" viewBox="0 0 342 130" role="img" aria-label="Slate Crest ring">
      <path class="body" d="M8,28.5 H32 C48,28.5 58,2 100,2 C142,2 152,28.5 168,28.5 H316 a8,8 0 0 1 8,8 V93.5 a8,8 0 0 1 -8,8 H168 C152,101.5 142,128 100,128 C58,128 48,101.5 32,101.5 H8 a8,8 0 0 1 -8,-8 V36.5 a8,8 0 0 1 8,-8 Z"/>
      <circle class="body" cx="324" cy="65" r="17"/>
      <line class="rule" x1="11" y1="44" x2="42" y2="44"/><line class="rule" x1="11" y1="85" x2="42" y2="85"/>
      <line class="rule" x1="150" y1="44" x2="306" y2="44"/><line class="rule" x1="150" y1="85" x2="306" y2="85"/>
      <text class="house-name" x="100" y="69" text-anchor="middle">TabacoMillDepot</text>
      <text class="label-name" x="228" y="72" text-anchor="middle">Slate Crest</text>
      <circle class="tab-ring" cx="324" cy="65" r="12"/>
    </svg>
  </section>

  <section class="foil-board" aria-label="Onyx Crest foil treatment">
    <svg width="911" height="479" viewBox="0 0 911 479">
      <line class="rule" x1="0" y1="170" x2="80" y2="170"/>
      <line class="rule" x1="0" y1="310" x2="80" y2="310"/>
      <line class="rule" x1="400" y1="170" x2="880" y2="170"/>
      <line class="rule" x1="400" y1="310" x2="880" y2="310"/>
      <text class="house-name" x="240" y="251" text-anchor="middle">TabacoMillDepot</text>
      <text class="label-name" x="640" y="260" text-anchor="middle">Onyx Crest</text>
    </svg>
  </section>
</main>
</body>
</html>
```